Redgum Wrecking P/L business card

I already have a EPS logo design that I wish to use however, the company is a demolition company based on the Central Coast of NSW Australia. The company is called "Redgum Wrecking P/L".

We offer demolition services such as Residential, Commercial, Civil, Asbestos removal, Excavation and Tree removal that are required to be displayed on the rear of the business card.

We currently have 4 personnel that require business cards with their specific contact details.

The logo is mid blue on a white background and the remainder is black text on a whiter card.

The eps logo supplied should only be displayed as a logo without the text.

Target Market(s)

People, governments, companies requiring demolition services on the east coast of NSW, specifically Central Coast, Sydney and Newcastle locations.

Industry/Entity Type

Business

Contact Information for Business Card

There are four cards required
First card:
Martin Ellory
Operations Director
Mobile No. 0451 872164
E: info@redgumwreck.example.com.au
www.redgumwreck.example.com.au
Second card:
Peter Hollis
Project Director
Company Mobile: 0451 872164
Personal Mobile: 0426 158 309
www.redgumwreck.example.com.au
Third card:
Simon Brady
Project Director
Company Mobile: 0451 872 164
Personal Mobile: 0433 917 482
www.redgumwreck.example.com.au
Fourth card:
Lewis Thornby
General Manager
Personal Mobile: 0447 261 835
www.redgumwreck.example.com.au

Font styles to use
Other font styles liked:
• Helvetica

Colors
33a6d7

Requirements
Must have
• The RW logo (without the text of Redgum Wrecking)
Horizontal layout with logo on top left hand corner
Services provision on the rear of the card
Nice to have
• Logo on top left corner
Text should be something like Helvetica
Should not have
• Do not include the text that is incorporated in the EPS file I sent ….just the logo

```html
<!DOCTYPE html>
<html lang="en">
<head>
<meta charset="utf-8">
<title>Redgum Wrecking P/L – Business Card</title>
<link rel="stylesheet" href="https://fonts.googleapis.com/css2?family=Questrial&display=swap">
<style>
  :root {
    --backdrop: #e4e4e2;
    --card: #ffffff;
    --card-tint: #f6f6f6;
    --ink: #111111;
    --ink-soft: #333333;
    --brand-blue: #33a6d7;
    --brand-faint: #d5dbe9;
    --shadow: rgba(0, 0, 0, 0.22);
  }
  * { margin: 0; padding: 0; box-sizing: border-box; }
  html, body {
    width: 1200px;
    height: 1000px;
    overflow: hidden;
    background: var(--backdrop);
    font-family: "Questrial", "Century Gothic", sans-serif;
    color: var(--ink);
  }
  .stage {
    position: relative;
    width: 1200px;
    height: 1000px;
  }
  .card {
    position: absolute;
    left: 250px;
    width: 700px;
    height: 420px;
    background: linear-gradient(180deg, var(--card-tint) 0%, var(--card) 45%, var(--card) 100%);
    box-shadow: 0 10px 28px var(--shadow);
  }
  .card--front { top: 50px; }
  .card--back { top: 530px; }

  /* Front */
  .brand {
    position: absolute;
    top: 44px;
    left: 48px;
    display: flex;
    align-items: center;
    gap: 12px;
  }
  .brand__mark {
    width: 22px;
    height: 22px;
    border-radius: 50%;
    background: var(--brand-blue);
  }
  .brand__name {
    font-size: 34px;
    line-height: 40px;
    letter-spacing: 1px;
    color: var(--brand-blue);
    text-transform: uppercase;
  }
  .person {
    position: absolute;
    left: 48px;
    top: 210px;
  }
  .person__name {
    font-size: 21px;
    font-weight: 700;
    color: var(--ink);
  }
  .person__role {
    margin-top: 4px;
    font-size: 16px;
    color: var(--ink-soft);
  }
  .contact {
    position: absolute;
    left: 48px;
    top: 285px;
    list-style: none;
  }
  .contact__item {
    display: flex;
    align-items: center;
    gap: 10px;
    font-size: 18px;
    line-height: 22px;
    color: var(--ink);
    margin-bottom: 10px;
  }
  .contact__icon { width: 18px; height: 18px; flex: none; }

  /* Back */
  .services {
    position: absolute;
    top: 44px;
    left: 0;
    width: 100%;
    text-align: center;
  }
  .services__intro {
    font-size: 22px;
    line-height: 28px;
    margin-bottom: 6px;
  }
  .services__list { list-style: none; }
  .services__item {
    font-size: 26px;
    line-height: 32px;
  }
  .services__item::before {
    content: "▪ ";
    font-size: 14px;
    vertical-align: middle;
  }
  .backmark {
    position: absolute;
    bottom: 32px;
    right: 48px;
    display: flex;
    align-items: center;
    gap: 12px;
  }
  .backmark__name {
    font-size: 34px;
    line-height: 40px;
    letter-spacing: 1px;
    color: var(--brand-faint);
    text-transform: uppercase;
  }
  .backmark__mark {
    width: 22px;
    height: 22px;
    border-radius: 50%;
    background: var(--brand-faint);
  }
</style>
</head>
<body>
<main class="stage">
  <section class="card card--front" aria-label="Business card front">
    <div class="brand">
      <span class="brand__mark"></span>
      <span class="brand__name">Redgum Wrecking</span>
    </div>
    <div class="person">
      <p class="person__name">Name Here</p>
      <p class="person__role">Position</p>
    </div>
    <ul class="contact">
      <li class="contact__item">
        <svg class="contact__icon" viewBox="0 0 20 20" aria-hidden="true">
          <path d="M2 7 Q10 1 18 7 L15 9 L13 6 L7 6 L5 9 Z" fill="#111"/>
          <rect x="4" y="10" width="12" height="7" rx="1.5" fill="#111"/>
          <circle cx="10" cy="13.5" r="2" fill="#fff"/>
        </svg>
        <span>0000000</span>
      </li>
      <li class="contact__item">
        <svg class="contact__icon" viewBox="0 0 20 20" aria-hidden="true">
          <rect x="1.5" y="4" width="17" height="12" fill="none" stroke="#111" stroke-width="1.8"/>
          <path d="M1.5 4 L10 11 L18.5 4" fill="none" stroke="#111" stroke-width="1.8"/>
        </svg>
        <span>email@redgumwreck.example.com.au</span>
      </li>
      <li class="contact__item">
        <svg class="contact__icon" viewBox="0 0 20 20" aria-hidden="true">
          <circle cx="10" cy="10" r="8" fill="none" stroke="#111" stroke-width="1.6"/>
          <ellipse cx="10" cy="10" rx="3.5" ry="8" fill="none" stroke="#111" stroke-width="1.4"/>
          <path d="M2 10 H18 M3.5 6 H16.5 M3.5 14 H16.5" stroke="#111" stroke-width="1.2"/>
        </svg>
        <span>redgumwreck.example.com.au</span>
      </li>
    </ul>
  </section>

  <section class="card card--back" aria-label="Business card back">
    <div class="services">
      <p class="services__intro">We offer demolition services:</p>
      <ul class="services__list">
        <li class="services__item">Residential</li>
        <li class="services__item">Commercial</li>
        <li class="services__item">Civil</li>
        <li class="services__item">Asbestos removal</li>
        <li class="services__item">Excavation</li>
        <li class="services__item">Tree removal</li>
      </ul>
    </div>
    <div class="backmark">
      <span class="backmark__mark"></span>
      <span class="backmark__name">Redgum Wrecking</span>
    </div>
  </section>
</main>
</body>
</html>
```